Business Card for a Renewable energy construction company

I need a formal, neat looking business card. Minimal and professional looking. Back side can have a design that is semi-ransparent/shaded

Target Market(s)

Renewable energy companies

Contact Information for Business Card

Name, Surname and contact details (phone, email)

Colors
00AB8E
00BBA5
67D7C9
C6EFE9
E9F9F6

Requirements
Must have
• Place for a QR code in the back side

```html
<!DOCTYPE html>
<html lang="en">
<head>
<meta charset="utf-8">
<title>Kalvera Business Card</title>
<link rel="stylesheet" href="https://fonts.googleapis.com/css2?family=Montserrat:wght@400;500;700&family=Open+Sans:wght@400&display=swap">
<style>
  :root {
    --teal: #3a9aa0;
    --teal-deep: #168a91;
    --ink: #282527;
    --paper: #ffffff;
    --table: #3b3b3d;
    --card-w: 880px;
    --card-h: 500px;
  }
  * { box-sizing: border-box; margin: 0; padding: 0; }
  html, body {
    width: 1200px; height: 1200px; overflow: hidden;
    background: var(--table);
  }
  .sheet {
    position: relative; width: 1200px; height: 1200px;
    display: flex; flex-direction: column; align-items: center; justify-content: center; gap: 70px;
  }
  .card {
    position: relative; width: var(--card-w); height: var(--card-h);
    border-radius: 40px; overflow: hidden;
    box-shadow: 0 0 0 3px var(--teal), 0 18px 40px rgba(0,0,0,.45);
  }

  /* front */
  .card--front { background: var(--ink); }
  .front__top {
    position: absolute; left: 0; top: 0; width: 100%; height: 262px;
    background: var(--paper);
    display: flex; align-items: center; justify-content: center;
  }
  .front__stripe {
    position: absolute; left: 0; top: 262px; width: 100%; height: 14px;
    background: var(--teal);
  }
  .brand { position: relative; z-index: 1; display: flex; align-items: center; gap: 18px; }
  .brand__mark { width: 46px; height: 46px; background: var(--teal); }
  .brand__name {
    font-family: "Montserrat", sans-serif; font-weight: 700;
    font-size: 74px; letter-spacing: 4px; line-height: 1;
  }
  .card--front .brand__name { color: var(--ink); }
  .card--back .brand__name { color: var(--paper); }

  .identity { position: absolute; left: 70px; top: 340px; }
  .identity__name {
    font-family: "Montserrat", sans-serif; font-weight: 500;
    font-size: 48px; color: var(--teal); line-height: 1;
  }
  .identity__role {
    font-family: "Montserrat", sans-serif; font-weight: 400;
    font-size: 30px; color: var(--paper); margin-top: 4px; letter-spacing: 1px;
  }
  .divider {
    position: absolute; left: 418px; top: 312px; width: 1px; height: 150px;
    background: #6a6668;
  }
  .contacts {
    position: absolute; left: 455px; top: 318px; list-style: none;
    font-family: "Open Sans", sans-serif; font-size: 25px; color: var(--paper);
  }
  .contacts li { display: flex; align-items: center; gap: 14px; height: 46px; }
  .contacts svg { width: 28px; height: 28px; flex: none; }

  /* back */
  .card--back {
    background: var(--ink);
    display: flex; align-items: center; justify-content: center;
  }
  .back__shade {
    position: absolute; inset: 0;
    background:
      linear-gradient(135deg, rgba(58,154,160,.16) 0%, rgba(58,154,160,0) 45%),
      linear-gradient(315deg, rgba(58,154,160,.12) 0%, rgba(58,154,160,0) 40%);
  }
  .back__band {
    position: absolute; left: -80px; bottom: 70px; width: 1100px; height: 60px;
    background: rgba(58,154,160,.08);
    transform: rotate(-8deg);
  }
  .qr-slot {
    position: absolute; right: 44px; bottom: 44px; z-index: 1;
    width: 104px; height: 104px;
    border: 2px solid var(--teal); border-radius: 6px;
    background: rgba(255,255,255,.06);
  }
</style>
</head>
<body>
<main class="sheet">
  <section class="card card--front" aria-label="Business card front">
    <div class="front__top">
      <div class="brand">
        <span class="brand__mark"></span>
        <span class="brand__name">KALVERA</span>
      </div>
    </div>
    <div class="front__stripe"></div>

    <div class="identity">
      <p class="identity__name">FULL NAME</p>
      <p class="identity__role">POSITION</p>
    </div>

    <div class="divider"></div>

    <ul class="contacts">
      <li>
        <svg viewBox="0 0 24 24" aria-hidden="true"><path fill="#3a9aa0" d="M6.6 10.8a15.1 15.1 0 0 0 6.6 6.6l2.2-2.2a1 1 0 0 1 1-.25 11.4 11.4 0 0 0 3.6.57 1 1 0 0 1 1 1V20a1 1 0 0 1-1 1A17 17 0 0 1 3 4a1 1 0 0 1 1-1h3.5a1 1 0 0 1 1 1c0 1.25.2 2.45.57 3.57a1 1 0 0 1-.25 1z"/></svg>
        <span>(000) 000 0000</span>
      </li>
      <li>
        <svg viewBox="0 0 24 24" aria-hidden="true"><rect x="2" y="5" width="20" height="14" fill="#3a9aa0"/><path d="M2 5l10 8 10-8" fill="none" stroke="#282527" stroke-width="1.6"/></svg>
        <span>email@company.com</span>
      </li>
      <li>
        <svg viewBox="0 0 24 24" aria-hidden="true" fill="none" stroke="#3a9aa0" stroke-width="1.8"><circle cx="12" cy="12" r="9.5"/><ellipse cx="12" cy="12" rx="4.2" ry="9.5"/><path d="M2.5 12h19M4 7h16M4 17h16"/></svg>
        <span>www.company.com</span>
      </li>
    </ul>
  </section>

  <section class="card card--back" aria-label="Business card back">
    <div class="back__shade" aria-hidden="true"></div>
    <div class="back__band" aria-hidden="true"></div>
    <div class="brand">
      <span class="brand__mark"></span>
      <span class="brand__name">KALVERA</span>
    </div>
    <div class="qr-slot" role="img" aria-label="Space for QR code"></div>
  </section>
</main>
</body>
</html>
```